Apricot Variety Sheet - Cedarline Orchard Growers

We are needing a variety sheet that we can hand out that will describe the different apricot vatieties we have available. The attached document has the name of the variety along with a description that will need to be on the sheet. We are looking for a modern, appealing way to display this information on 1 page (if needed, it can be front and back)
Updates

Apologies for the delay; we are overwhelmed with the great design options and will be sorting through them all (across our contests) to pick a collective. Thank you for your patience.

Target Market(s)

Growers and consumers

Industry/Entity Type

Agriculture

Requirements
Must have
• Easy to read
• Natural color palettes to emphasize the agricultural nature
• Clearly show washington as the origin in the title or at the top
Nice to have
• incorporate Apricots in the design

```html
<!DOCTYPE html>
<html lang="en">
<head>
<meta charset="utf-8">
<title>Apricot Variety Sheet – Cedarline Orchard Growers</title>
<link href="https://fonts.googleapis.com/css2?family=Lato:wght@400;700;900&family=Oswald:wght@600&display=swap" rel="stylesheet">
<style>
  :root {
    --green-dark: #0f5a2c;
    --green: #1c6b3a;
    --green-light: #5a9a12;
    --red: #d0261d;
    --red-dark: #8e1a14;
    --orange: #f0883a;
    --ink: #2c2c2c;
    --block: #2a2a2a;
    --panel-top: #f4f4f4;
    --panel-bottom: #dcdcdc;
    --white: #ffffff;
  }
  * { box-sizing: border-box; margin: 0; padding: 0; }
  html, body { width: 902px; height: 1200px; overflow: hidden; background: var(--white); }
  body { font-family: "Lato", Arial, sans-serif; color: var(--ink); }

  .sheet { position: relative; width: 902px; height: 1200px; background: var(--white); overflow: hidden; }

  /* Header */
  .header { position: absolute; top: 0; left: 0; width: 902px; height: 100px; background: var(--white); }
  .header-band { position: absolute; top: 0; right: 0; width: 470px; height: 96px;
    background: linear-gradient(90deg, var(--green-light), var(--green) 70%, var(--green-dark));
    clip-path: polygon(0 0, 100% 0, 100% 100%, 60px 100%); }
  .brand { position: absolute; left: 62px; top: 18px; display: flex; align-items: center; gap: 14px; }
  .brand-dot { width: 62px; height: 62px; border-radius: 50%; background: var(--orange); }
  .brand-name { font-weight: 700; font-size: 22px; line-height: 24px; color: var(--green); }
  .header-rule { position: absolute; top: 102px; left: 0; width: 902px; height: 5px; background: var(--red-dark); }

  /* Hero */
  .hero { position: absolute; top: 110px; left: 0; width: 902px; height: 290px; }
  .hero-wedge { position: absolute; left: 0; top: 8px; width: 204px; height: 280px;
    background: linear-gradient(135deg, var(--orange), var(--red));
    clip-path: polygon(0 0, 0 100%, 100% 100%); }
  .hero-title { position: absolute; left: 82px; top: 16px; z-index: 2;
    font-family: "Oswald", "Arial Narrow", sans-serif;
    font-weight: 600; font-size: 90px; line-height: 1; letter-spacing: 0;
    color: var(--green); transform: scaleX(0.86); transform-origin: left top; white-space: nowrap; }
  .fruit-small { position: absolute; left: 262px; top: 122px; width: 258px; height: 150px; border-radius: 75px;
    background: radial-gradient(ellipse at 45% 50%, #f7a23a, #f5c070 55%, rgba(255,255,255,0) 72%); }
  .fruit-large { position: absolute; left: 520px; top: 14px; width: 358px; height: 262px; border-radius: 130px;
    background: radial-gradient(ellipse at 50% 55%, #f08a2e, #ee7a5a 42%, #f6c79a 60%, rgba(255,255,255,0) 72%); }

  /* Title band */
  .title-band { position: absolute; top: 400px; left: 0; width: 902px; height: 52px;
    background: linear-gradient(90deg, var(--green-dark), var(--green) 50%, var(--green-light));
    display: flex; align-items: center; justify-content: center; }
  .title-band h1 { font-weight: 700; font-size: 32px; color: var(--white); letter-spacing: 0.5px; margin-left: 10px; }

  /* Varieties */
  .varieties { position: absolute; top: 452px; left: 0; width: 902px; height: 690px; }
  .column { position: absolute; top: 0; height: 690px; padding-top: 22px; }
  .column-left { left: 0; width: 468px;
    background: linear-gradient(180deg, var(--panel-top), var(--panel-bottom));
    box-shadow: 4px 0 8px rgba(0,0,0,0.22); z-index: 1; }
  .column-right { left: 462px; width: 440px; padding-left: 0; }
  .variety { position: relative; height: 113px; padding: 27px 38px 0 38px; }
  .column-right .variety { padding-left: 50px; padding-right: 28px; }
  .variety-block { position: absolute; left: 0; top: 0; width: 30px; height: 58px; background: var(--block); }
  .column-right .variety-block { left: 12px; }
  .variety-name { position: absolute; left: 30px; top: 0; height: 18px; padding: 0 34px 0 8px;
    background: var(--red); color: var(--white); font-weight: 700; font-size: 14px; line-height: 18px;
    text-transform: uppercase; letter-spacing: 0.3px;
    clip-path: polygon(0 0, 100% 0, calc(100% - 14px) 100%, 0 100%); }
  .column-right .variety-name { left: 42px; }
  .variety-text { font-size: 14px; line-height: 17px; text-align: justify; }

  /* Footer */
  .footer-rule { position: absolute; top: 1142px; left: 0; width: 902px; height: 4px; background: var(--red); }
  .footer { position: absolute; top: 1146px; left: 0; width: 902px; height: 54px;
    background: linear-gradient(90deg, var(--green-dark), var(--green) 50%, var(--green-light));
    display: flex; align-items: center; justify-content: center; gap: 10px; }
  .footer svg { width: 22px; height: 22px; }
  .web { font-weight: 700; font-size: 20px; letter-spacing: 5px; color: var(--white); }
</style>
</head>
<body>
<div class="sheet">
  <header class="header">
    <div class="brand">
      <span class="brand-dot"></span>
      <span class="brand-name">Cedarline Orchard<br>Growers</span>
    </div>
    <div class="header-band"></div>
  </header>
  <div class="header-rule"></div>

  <section class="hero">
    <div class="hero-wedge"></div>
    <div class="fruit-small" role="img" aria-label="Photo of whole and halved apricots with leaves"></div>
    <div class="fruit-large" role="img" aria-label="Photo of ripe blushed apricots, one cut in half showing the stone"></div>
    <div class="hero-title">WASHINGTON</div>
  </section>

  <div class="title-band"><h1>APRICOT VARIETY SHEET</h1></div>

  <main class="varieties">
    <div class="column column-left">
      <article class="variety"><span class="variety-block"></span><h2 class="variety-name">Rival</h2>
        <p class="variety-text">Great flavor with a fine, firm texture distinguishes this large oval-shaped apricot. The skin is light orange with a red blush. The flesh is a lush deep orange color. Available early July-early August.</p></article>
      <article class="variety"><span class="variety-block"></span><h2 class="variety-name">Robada</h2>
        <p class="variety-text">This jumbo apricot has a delicious floral flavor with a firm texture. Bright orange, with a deep red blush over nearly half its surface. Available early June.</p></article>
      <article class="variety"><span class="variety-block"></span><h2 class="variety-name">Perfection</h2>
        <p class="variety-text">This classic large oval apricot is deep orange with an oblong shape and firm texture. The flesh is a yellow/orange color that is very sweet and full of flavor. Available mid July - mid August.</p></article>
      <article class="variety"><span class="variety-block"></span><h2 class="variety-name">Patterson</h2>
        <p class="variety-text">This apricot has a well-balanced flavor and an excellent shelf life. This is perfect for canning or drying. It has streaked red over yellow skin, with a firm flesh. Available mid – late June.</p></article>
      <article class="variety"><span class="variety-block"></span><h2 class="variety-name">Tomcot</h2>
        <p class="variety-text">Tangy, sweet flavor with a firm texture. This oval apricot is light orange with a slight blush color. The flesh is a dark orange. Available late June – late July.</p></article>
      <article class="variety"><span class="variety-block"></span><h2 class="variety-name">Goldrich</h2>
        <p class="variety-text">This apricot is round with a bright orange skin color and a deep orange flesh. It has a mild, sweet flavor with a firm texture. Available early July – mid August.</p></article>
    </div>

    <div class="column column-right">
      <article class="variety"><span class="variety-block"></span><h2 class="variety-name">Casselbrite</h2>
        <p class="variety-text">This medium sized apricot is golden orange with a slight red blush. It has a mild sweet-tart flavor that is good for eating out of hand. Available late June- early July.</p></article>
      <article class="variety"><span class="variety-block"></span><h2 class="variety-name">Goldbar</h2>
        <p class="variety-text">Moderately juicy, this large oval-shaped apricot has a light yellow-orange with a reddish blush. The flesh is firm, meaty, and has a light orange color. Available late June – end of July.</p></article>
      <article class="variety"><span class="variety-block"></span><h2 class="variety-name">Sweet Juillet</h2>
        <p class="variety-text">This special variety has a unique, sweet flavor with a juicy flesh. It is bright orange in color with a bright orange flesh. Available through July.</p></article>
      <article class="variety"><span class="variety-block"></span><h2 class="variety-name">Tasty Rich</h2>
        <p class="variety-text">This early variety is light yellow-orange colored with a firm texture. Very juicy with an enticing flavor. Available through June.</p></article>
      <article class="variety"><span class="variety-block"></span><h2 class="variety-name">Goldstrike</h2>
        <p class="variety-text">A larger apricot with light orange, blushed skin. Firm texture with a slight tart taste until fully ripened, then very sweet. Available mid June - mid July.</p></article>
      <article class="variety"><span class="variety-block"></span><h2 class="variety-name">Riland</h2>
        <p class="variety-text">Very aromatic and sweet, this apricot is orange with a red blush. It has a yellow-orange colored flesh and a round shape. Available mid-June to end of July.</p></article>
    </div>
  </main>

  <div class="footer-rule"></div>
  <footer class="footer">
    <svg viewBox="0 0 24 24" aria-hidden="true" fill="none" stroke="#ffffff" stroke-width="1.6">
      <circle cx="12" cy="12" r="10"/>
      <ellipse cx="12" cy="12" rx="4.5" ry="10"/>
      <line x1="2" y1="12" x2="22" y2="12"/>
      <line x1="4" y1="6.5" x2="20" y2="6.5"/>
      <line x1="4" y1="17.5" x2="20" y2="17.5"/>
    </svg>
    <span class="web">cedarlineorchard.com</span>
  </footer>
</div>
</body>
</html>
```